Healthcare Technology Company Business Card Design

Hi,

We require a new business card design thats catchy and professional.
Our target audience is healthcare professionals. See supplied artwork for our logo.

If you think its achievable please try add the tag line, not necessary however.
"Developing technologies to improve patient care and release operation benefits"

We'll require the following information on the card. No need to have the subject titles but i've referenced them for your convenience.

Personal Details
Mark Towler
Position: Director
Phone Number - 03 9471 5382
Mobile Number - 0427 836 259
Email: firstname.lastname@velkarin.com.au

Company Details
Suite 38, 216 Wendrell Street
Port Melbourne, Victoria
Fax: 03 8214 3975
velkarin.com.au

Prefer a thinner design than the normal stock standard business card dimensions.
Please ensure there is adequate bleed.

Target Market(s)

Healthcare Professionals

Industry/Entity Type

Healthcare

Font styles to use
Sans Serif

Requirements
Must have
• Clean, Sharp Looks
Should not have
• Any healthcare symbols

```html
<!DOCTYPE html>
<html lang="en">
<head>
<meta charset="utf-8">
<title>Velkarin Business Card</title>
<link href="https://fonts.googleapis.com/css2?family=Open+Sans:ital,wght@0,400;0,600;0,700;1,400&display=swap" rel="stylesheet">
<style>
  :root {
    --backdrop: #3a3d3c;
    --card: #f7f7f5;
    --navy: #456a94;
    --navy-dark: #3a5a80;
    --amber: #f0a830;
    --ink: #4a4a4a;
    --muted: #7a7a7a;
  }
  * { box-sizing: border-box; margin: 0; padding: 0; }
  html, body { width: 1200px; height: 1000px; overflow: hidden; }
  body {
    background: var(--backdrop);
    font-family: "Open Sans", sans-serif;
    display: flex; flex-direction: column; align-items: center; justify-content: center;
    gap: 60px;
  }
  .card {
    position: relative; width: 780px; height: 420px;
    background: var(--card); overflow: hidden;
    box-shadow: 0 10px 30px rgba(0,0,0,.35);
  }
  .brand { display: flex; align-items: center; gap: 14px; }
  .brand-mark { width: 34px; height: 34px; background: var(--amber); }
  .brand-name { font-weight: 600; color: var(--navy); letter-spacing: -0.5px; }

  /* back */
  .card-back .colour-block {
    position: absolute; right: 0; top: 0; width: 250px; height: 100%;
    background: var(--navy);
  }
  .card-back .colour-block::before {
    content: ""; position: absolute; left: 0; top: 0; width: 100%; height: 90px;
    background: var(--amber);
  }
  .card-back .brand { position: absolute; left: 70px; top: 150px; }
  .card-back .brand-name { font-size: 58px; }
  .card-back .brand-mark { width: 52px; height: 52px; }
  .web { position: absolute; left: 170px; top: 290px; font-size: 20px; font-weight: 700; color: var(--navy); }
  .web .bracket { color: var(--amber); }

  /* front */
  .card-front .colour-block {
    position: absolute; left: 0; top: 0; width: 220px; height: 330px;
    background: var(--navy);
  }
  .card-front .colour-block::before {
    content: ""; position: absolute; left: 0; top: 0; width: 100%; height: 70px;
    background: var(--amber);
  }
  .details { position: absolute; left: 270px; right: 40px; top: 34px; text-align: center; }
  .details .brand { justify-content: center; }
  .details .brand-name { font-size: 36px; }
  .tagline { margin-top: 8px; font-style: italic; color: var(--muted); font-size: 15px; line-height: 1.3; }
  .person { margin-top: 20px; }
  .person-name { font-size: 30px; font-weight: 700; color: var(--navy); line-height: 1.1; }
  .person-role { color: var(--muted); font-size: 14px; }
  .contact { margin-top: 12px; display: inline-grid; grid-template-columns: auto auto; column-gap: 12px; text-align: left; font-size: 15px; line-height: 1.25; color: var(--ink); }
  .label { color: var(--navy); font-weight: 700; }
  .email { margin-top: 8px; font-size: 15px; color: var(--ink); }
  .rule { position: absolute; left: 30px; right: 30px; top: 345px; height: 2px; background: var(--amber); }
  .address { position: absolute; left: 30px; right: 30px; top: 365px; font-size: 15px; color: var(--ink); white-space: nowrap; }
</style>
</head>
<body>
  <section class="card card-back">
    <div class="colour-block"></div>
    <div class="brand">
      <span class="brand-mark"></span>
      <span class="brand-name">Velkarin</span>
    </div>
    <p class="web"><span class="bracket">[</span>www.velkarin.com.au<span class="bracket">]</span></p>
  </section>

  <section class="card card-front">
    <div class="colour-block"></div>
    <div class="details">
      <div class="brand">
        <span class="brand-mark"></span>
        <span class="brand-name">Velkarin</span>
      </div>
      <p class="tagline">“Developing technologies to improve patient care<br>&amp; release operation benefits”</p>
      <div class="person">
        <p class="person-name">Mark Towler</p>
        <p class="person-role">[Director]</p>
      </div>
      <div class="contact">
        <span class="label">[Phone]</span><span>03 9471 5382</span>
        <span class="label">[Mobile]</span><span>0427 836 259</span>
      </div>
      <p class="email">mark.towler@velkarin.com.au</p>
    </div>
    <div class="rule"></div>
    <p class="address"><span class="label">[Address]</span> Suite 38 | 216 Wendrell Street Port Melbourne | Victoria <span class="label">[Fax]</span> 03 8214 3975</p>
  </section>
</body>
</html>
```